Wood Logging Stationary design

We need a new company logo for our stationary. Be creative. Most company apparel and hats are Navy blue and Light gray. Logo does not necessarily have to contain those two colors. Pictures of trees, logging equipment, log trucks, and logs are acceptable but not required. I am open to any and all designs. Logo must reflect our pride and professionalism in the East Texas Timber Industry.
Updates

Target Market(s)

Timber owners and sawmills. Adults 25 years and up

Industry/Entity Type

Industry

Font styles to use
Serif
Decorative

Requirements
Must have
• R. J. Pell Hauling Co.
Nice to have
• Phone number: 936-402-5817
address:
PO Box 4830
Dunmore Flats, TX 77912
www.rjpellhauling.example
rjpellhauling@mailbox.example

```html
<!DOCTYPE html>
<html lang="en">
<head>
<meta charset="utf-8">
<title>R. J. Pell Hauling Co. — Stationery</title>
<link rel="stylesheet" href="https://fonts.googleapis.com/css2?family=Oswald:wght@400;500&display=swap">
<style>
  :root {
    --backdrop: #dcdddc;
    --paper: #e9eeec;
    --ink: #111111;
    --window: #d6dadb;
    --backing: #000000;
  }
  * { box-sizing: border-box; margin: 0; padding: 0; }
  html, body { width: 1200px; height: 900px; overflow: hidden; }
  body {
    position: relative;
    background: var(--backdrop);
    font-family: "Oswald", "Arial Narrow", sans-serif;
    color: var(--ink);
  }
  .sheet { position: absolute; background: var(--paper); }
  .brand-name {
    font-weight: 500;
    text-transform: uppercase;
    letter-spacing: 0.02em;
    white-space: nowrap;
    line-height: 1;
    text-align: center;
  }
  .contact { font-weight: 400; line-height: 1.3; white-space: nowrap; }

  /* Envelope */
  .envelope { left: 80px; top: 88px; width: 483px; height: 244px; }
  .envelope .brand-name { position: absolute; left: 150px; top: 35px; width: 0; display: flex; justify-content: center; font-size: 15px; }
  .envelope .contact { position: absolute; left: 113px; top: 80px; font-size: 7px; }
  .envelope .address-window {
    position: absolute; left: 41px; top: 117px; width: 205px; height: 86px;
    background: var(--window); border-radius: 4px;
  }
  .envelope .web-line { position: absolute; left: 45px; top: 215px; font-size: 7px; }

  /* Business cards */
  .card { width: 197px; height: 111px; top: 360px; }
  .card-front { left: 138px; }
  .card-back { left: 365px; }
  .card-front .brand-name { position: absolute; left: 0; right: 0; top: 48px; font-size: 13px; }
  .card-back .brand-name { position: absolute; left: 0; right: 0; top: 20px; font-size: 9px; }
  .card-back .contact { position: absolute; left: 68px; top: 48px; font-size: 7px; }
  .card-back .web-line { position: absolute; left: 54px; top: 81px; font-size: 7px; line-height: 1.3; }

  /* Letterhead */
  .backing { position: absolute; left: 660px; top: 88px; width: 460px; height: 652px; background: var(--backing); }
  .letterhead { left: 593px; top: 155px; width: 460px; height: 651px; }
  .letterhead .brand-name { position: absolute; left: 46px; width: 154px; top: 74px; font-size: 19px; display: flex; justify-content: center; }
  .letterhead .contact { position: absolute; left: 293px; top: 38px; font-size: 11px; }
  .letterhead .web-line { position: absolute; left: 265px; top: 93px; font-size: 11px; line-height: 1.25; }
  .letterhead .web-line span { display: block; padding-left: 29px; }
  .letterhead .rule { position: absolute; left: 13px; right: 13px; top: 159px; height: 7px; background: var(--ink); }
</style>
</head>
<body>

  <section class="sheet envelope" aria-label="Envelope">
    <div class="brand-name">R. J. Pell Hauling Co.</div>
    <p class="contact">Phone // 936-402-5817<br>PO Box 4830<br>Dunmore Flats, TX 77912</p>
    <div class="address-window"></div>
    <p class="contact web-line">web // www.rjpellhauling.example // rjpellhauling@mailbox.example</p>
  </section>

  <section class="sheet card card-front" aria-label="Business card front">
    <div class="brand-name">R. J. Pell Hauling Co.</div>
  </section>

  <section class="sheet card card-back" aria-label="Business card back">
    <div class="brand-name">R. J. Pell Hauling Co.</div>
    <p class="contact">Phone // 936-402-5817<br>PO Box 4830<br>Dunmore Flats, TX 77912</p>
    <p class="contact web-line">web // www.rjpellhauling.example<br>&nbsp;&nbsp;&nbsp;&nbsp;&nbsp;&nbsp;&nbsp;rjpellhauling@mailbox.example</p>
  </section>

  <div class="backing" aria-hidden="true"></div>
  <section class="sheet letterhead" aria-label="Letterhead">
    <div class="brand-name">R. J. Pell Hauling Co.</div>
    <p class="contact">Phone // 936-402-5817<br>PO Box 4830<br>Dunmore Flats, TX 77912</p>
    <p class="contact web-line">web // www.rjpellhauling.example<span>rjpellhauling@mailbox.example</span></p>
    <div class="rule"></div>
  </section>

</body>
</html>
```